Letterhead Design Project

I need a letterhead design that is simple, modern, and colorful.

We publish novels that speak to female empowerment. With our fiction, we hope to encourage women to live boldly and love themselves without apology.

Our logo is red and teal so I'd like to see those colors continued in the letterhead.

The final design should be bold and inspiring.
Updates

Hello talented designers!

We will also be needing a business card design which will hopefully go to the designer of our letterhead. Please keep that in mind.

Thanks for all your efforts (in advance)!

I'd like the following information included:

Address - 4716 North Pellham Street, Suite #208, Chicago Ridge, Illinois 60415
Website - www.quillmarshpress.example
Email - info@quillmarshpress.example

Please see the updated files. The part of the logo that was red is now pink. And I've uploaded .eps and .ai formats. Thanks.

Target Market(s)

women, age 25+, college educated professionals

Requirements
Nice to have
• swirls or flourishes
Should not have
• dots or stripes

```html
<!DOCTYPE html>
<html lang="en">
<head>
<meta charset="utf-8">
<title>Quillmarsh Press Letterhead</title>
<link rel="stylesheet" href="https://fonts.googleapis.com/css2?family=EB+Garamond:wght@500&family=PT+Sans:wght@400&display=swap">
<style>
  :root {
    --paper: #ffffff;
    --teal: #93fce0;
    --red: #fb0512;
    --sliver: #b9bcbc;
    --brand: #8a1418;
    --watermark: #f6eef0;
    --ink: #111111;
  }
  html, body {
    margin: 0;
    padding: 0;
    overflow: hidden;
    background: var(--paper);
  }
  .letterhead {
    position: relative;
    width: 927px;
    height: 1200px;
    overflow: hidden;
    background: var(--paper);
  }
  .letterhead__bands {
    position: absolute;
    inset: 0;
  }
  .band--teal { fill: var(--teal); }
  .band--red { fill: var(--red); }
  .band--sliver { fill: var(--sliver); }
  .brand-mark {
    position: absolute;
    top: 100px;
    left: 642px;
    width: 16px;
    height: 16px;
    border-radius: 50%;
    background: var(--brand);
  }
  .brand {
    position: absolute;
    top: 98px;
    left: 664px;
    font-family: "EB Garamond", Georgia, serif;
    font-weight: 500;
    font-size: 19px;
    line-height: 20px;
    color: var(--brand);
    white-space: nowrap;
  }
  .watermark {
    position: absolute;
    top: 540px;
    left: 0;
    width: 927px;
    text-align: center;
    font-family: "EB Garamond", Georgia, serif;
    font-weight: 500;
    font-size: 96px;
    color: var(--watermark);
    white-space: nowrap;
  }
  .contact {
    position: absolute;
    top: 1076px;
    left: 214px;
    width: 500px;
    text-align: center;
    font-family: "PT Sans", Arial, sans-serif;
    font-style: normal;
    font-weight: 400;
    font-size: 14px;
    line-height: 18px;
    color: var(--ink);
  }
  .contact p { margin: 0; }
</style>
</head>
<body>
  <main class="letterhead">
    <svg class="letterhead__bands" width="927" height="1200" viewBox="0 0 927 1200" aria-hidden="true">
      <polygon class="band--teal" points="0,0 840,0 840,10 0,91"/>
      <polygon class="band--sliver" points="835,0 927,0 927,8 836,8"/>
      <polygon class="band--red" points="836,8 927,8 927,927"/>
    </svg>

    <div class="brand-mark" aria-hidden="true"></div>
    <div class="brand">Quillmarsh Press</div>

    <div class="watermark" aria-hidden="true">Quillmarsh</div>

    <address class="contact">
      <p>4716 North Pellham Street, Suite #208,</p>
      <p>Chicago Ridge, Illinois 60415</p>
      <p>www.quillmarshpress.example&nbsp;&nbsp; info@quillmarshpress.example</p>
    </address>
  </main>
</body>
</html>
```